Velvet Lumina Dance/Tantra/ Circles/ Performer Business Card design

Velvet Lumina is a brand. I offer Velvet Veil Sway, Velvet Lumina Dance, Velvet Lumina Tantra, and Velvet Lumina Hoop/ Pole performance.
I utilise yoga philosophy with veils, the moon, and naked bodies. I would like a naked goddess with a veil looking up at moon with sacred geometry included eg flower of life. My work is offered to women who are wanting to connect to their inner goddess and for men/women wanting to connect to their sacred sexuality. Would love a naked goddess to face moon with veil covering her body slightly. She is to look powerful, graceful...goddess. Colour scheme wise...love the deeper purples....silver would look good...maybe have veil with flower of life design/or flower of life design somehow incorporated into the moon/sky. It is to look powerful, sunual, alluring....not fluffly.

Target Market(s)

spiritual seekers

Industry/Entity Type

Business

Contact Information for Business Card

Velvet Lumina
"My mission is to empower, explore, and love the inner goddess through dance and sacred sexuality" Mira Tollworth
www.velvetlumina-example.com.au
ph: 0471203958

Logo Text

Velvet Lumina

Logo styles of interest
Pictorial/Combination Logo
Requirements
Must have
• moon, naked woman, veil, sacred geometry
Nice to have
• chakras lotus

```html
<!DOCTYPE html>
<html lang="en">
<head>
<meta charset="utf-8">
<title>Velvet Lumina Business Card</title>
<link rel="stylesheet" href="https://fonts.googleapis.com/css2?family=EB+Garamond:wght@400;500&display=swap">
<style>
  :root {
    --page: #ffffff;
    --plum-deep: #2e0636;
    --plum: #5a1466;
    --plum-bright: #7d2a8c;
    --orchid: #8b2c95;
    --silver: #f3f0f5;
    --gray-text: #6a6a6a;
    --gold: #c9a80c;
    --card-white: #ffffff;
    --pattern-tint: #ececee;
    --shadow: rgba(0, 0, 0, 0.18);
  }
  * { margin: 0; padding: 0; box-sizing: border-box; }
  html, body {
    width: 1200px;
    height: 460px;
    overflow: hidden;
    background: var(--page);
    font-family: "EB Garamond", Garamond, serif;
  }
  .canvas { position: relative; width: 1200px; height: 460px; }

  .card {
    position: absolute;
    top: 46px;
    height: 323px;
    overflow: hidden;
  }
  .card-shadow {
    position: absolute;
    top: 384px;
    height: 16px;
    border-radius: 50%;
    background: radial-gradient(ellipse at center, var(--shadow) 0%, rgba(0,0,0,0) 70%);
  }

  /* Front */
  .card-front { left: 30px; width: 543px; }
  .front-backdrop {
    position: absolute; inset: 0;
    background: radial-gradient(ellipse 60% 70% at 52% 55%, var(--plum-bright) 0%, var(--plum) 45%, var(--plum-deep) 100%);
  }
  .front-geometry {
    position: absolute;
    left: 126px; top: 8px;
    width: 300px; height: 300px;
    border-radius: 50%;
    background: radial-gradient(circle, rgba(255,255,255,0.06) 0%, rgba(255,255,255,0.02) 70%, rgba(255,255,255,0) 100%);
  }
  .front-mark {
    position: absolute;
    left: 0; right: 0; top: 56px;
    display: flex; flex-direction: column; align-items: center; gap: 22px;
  }
  .front-mark .mark-dot {
    width: 120px; height: 120px;
    border-radius: 50%;
    background: var(--silver);
  }
  .brand-name {
    color: var(--silver);
    font-size: 44px;
    font-weight: 400;
    letter-spacing: 0.5px;
    line-height: 1;
  }

  /* Back */
  .card-back { left: 618px; width: 547px; background: var(--card-white); box-shadow: 0 0 0 1px #e6e6e6; }
  .back-backdrop {
    position: absolute; inset: 0;
    background: radial-gradient(ellipse 80% 90% at 55% 30%, var(--card-white) 0%, var(--pattern-tint) 100%);
  }
  .back-mark {
    position: absolute;
    left: 12px; top: 80px; width: 210px;
    display: flex; flex-direction: column; align-items: center; gap: 14px;
  }
  .back-mark .mark-dot {
    width: 90px; height: 90px; border-radius: 50%;
    background: var(--orchid);
  }
  .back-mark .brand-name { color: var(--orchid); font-size: 26px; }
  .divider {
    position: absolute;
    left: 244px; top: 62px;
    width: 2px; height: 180px;
    background: linear-gradient(to bottom, rgba(180,180,180,0), #c8c8c8 30%, #c8c8c8 70%, rgba(180,180,180,0));
  }
  .contact {
    position: absolute;
    left: 270px; top: 92px;
  }
  .contact-name {
    color: var(--orchid);
    font-size: 41px;
    font-weight: 400;
    line-height: 1;
    margin-bottom: 14px;
  }
  .contact-line {
    display: flex; align-items: center; gap: 6px;
    color: var(--gray-text);
    font-size: 23px;
    line-height: 31px;
  }
  .contact-line svg { flex: none; }
  .gold-rule {
    position: absolute; left: 0; right: 0; top: 276px;
    height: 5px; background: var(--gold);
  }
  .web-band {
    position: absolute; left: 0; right: 0; top: 281px; bottom: 0;
    background: linear-gradient(to bottom, var(--orchid), var(--plum));
    display: flex; align-items: center; justify-content: center;
    color: var(--card-white);
    font-size: 22px;
  }
</style>
</head>
<body>
<main class="canvas">
  <section class="card card-front">
    <div class="front-backdrop" role="img" aria-label="Deep purple background with a faint sacred geometry flower of life pattern"></div>
    <div class="front-geometry" role="img" aria-label="Faint circular flower of life ornament"></div>
    <div class="front-mark">
      <span class="mark-dot"></span>
      <span class="brand-name">VELVET LUMINA</span>
    </div>
  </section>
  <div class="card-shadow" style="left:50px;width:500px;"></div>

  <section class="card card-back">
    <div class="back-backdrop" role="img" aria-label="White background with a faint grey flower of life pattern"></div>
    <div class="back-mark">
      <span class="mark-dot"></span>
      <span class="brand-name">Velvet Lumina</span>
    </div>
    <div class="divider"></div>
    <div class="contact">
      <p class="contact-name">Mira Tollworth</p>
      <p class="contact-line">
        <svg width="20" height="14" viewBox="0 0 20 14" aria-hidden="true">
          <rect x="0" y="0" width="20" height="14" fill="#8a8a8a"/>
          <path d="M0 0 L10 8 L20 0" fill="none" stroke="#ffffff" stroke-width="1.6"/>
        </svg>
        hello@example-mail.com
      </p>
      <p class="contact-line">
        <svg width="20" height="20" viewBox="0 0 20 20" aria-hidden="true">
          <path d="M5 2 L8 6 L6.5 8 C7.5 10.5 9.5 12.5 12 13.5 L14 12 L18 15 L16 18 C10 18 2 10 2 4 Z" fill="#8a8a8a"/>
        </svg>
        Phone: 0471203958
      </p>
    </div>
    <div class="gold-rule"></div>
    <div class="web-band">www.velvetlumina-example.com.au</div>
  </section>
  <div class="card-shadow" style="left:640px;width:505px;"></div>
</main>
</body>
</html>
```